Signage. Will be for store front. Building is on a corner lot. Lots of traffic.

Opening a new location for our landscape business with a garden store (boutique theme) which will have big pottery pots, house plants, ferns and orchids for sale.

And on the side lot of the store we will have bigger bulk items(contractors theme) landscape plants, sod, mulch, soil, rock for sale.

Sign is about 8’x6’

Target Market(s)

Home owners
Landscapers
Builders

Industry/Entity Type

Landscaping

Font styles to use
Sans Serif

Colors
9bcb3c

Requirements
Must have
• “ Installation and Delivery” is a big deal to let people know we do that
Nice to have
• Added a first rendition idea but don’t love it
Added a file with some words to play with
Need help with the words
Should not have
• ?

```html
<!DOCTYPE html>
<html lang="en">
<head>
<meta charset="utf-8">
<title>Brightleaf Outdoors – Storefront Sign</title>
<link rel="stylesheet" href="https://fonts.googleapis.com/css2?family=Montserrat:wght@700;800&family=Oswald:wght@600&display=swap">
<style>
  :root {
    --page-bg: #e4e4e4;
    --sign-white: #ffffff;
    --brand-green: #6f9a33;
    --band-green-light: #7fa338;
    --band-green-dark: #3f6b1c;
    --band-yellow: #e0b820;
    --ink: #161616;
    --photo-light: #93ad62;
    --photo-dark: #55722f;
  }
  * { box-sizing: border-box; margin: 0; padding: 0; }
  html, body { width: 800px; height: 1200px; overflow: hidden; }
  body { background: var(--page-bg); position: relative; }

  .sign {
    position: absolute;
    left: 40px; top: 330px;
    width: 720px; height: 540px;
    background: var(--sign-white);
    overflow: hidden;
    box-shadow: 0 10px 30px rgba(0,0,0,0.25);
  }
  .sign-art { position: absolute; inset: 0; }

  .brand-name {
    position: absolute;
    left: 50px; top: 44px;
    font-family: "Montserrat", sans-serif;
    font-weight: 700;
    font-size: 44px;
    line-height: 52px;
    letter-spacing: 1px;
    color: var(--brand-green);
    text-transform: uppercase;
  }

  .services {
    position: absolute;
    left: 0; top: 0;
    list-style: none;
    font-family: "Montserrat", sans-serif;
    font-weight: 800;
    font-size: 46px;
    color: var(--sign-white);
  }
  .service {
    position: absolute;
    left: 89px;
    white-space: nowrap;
    line-height: 1;
  }
  .service--sod { top: 200px; }
  .service--lawn { top: 200px; left: 245px; }
  .service--garden { top: 264px; }
  .service--landscape { top: 329px; }

  .phone {
    position: absolute;
    left: 112px; top: 408px;
    font-family: "Montserrat", sans-serif;
    font-weight: 800;
    font-size: 42px;
    line-height: 1;
    color: var(--ink);
    white-space: nowrap;
  }

  .tagline {
    position: absolute;
    left: 56px; top: 482px;
    font-family: "Oswald", sans-serif;
    font-weight: 600;
    font-size: 38px;
    line-height: 1;
    color: var(--ink);
    text-transform: uppercase;
    white-space: nowrap;
  }
</style>
</head>
<body>
  <div class="sign">
    <svg class="sign-art" width="720" height="540" viewBox="0 0 720 540" aria-hidden="false">
      <defs>
        <linearGradient id="bandGreen" x1="0" y1="0" x2="1" y2="1">
          <stop offset="0" stop-color="var(--band-green-light)"/>
          <stop offset="0.6" stop-color="#6b9530"/>
          <stop offset="1" stop-color="var(--band-green-dark)"/>
        </linearGradient>
        <linearGradient id="photoTone" x1="0" y1="0" x2="0.6" y2="1">
          <stop offset="0" stop-color="var(--photo-light)"/>
          <stop offset="1" stop-color="var(--photo-dark)"/>
        </linearGradient>
      </defs>

      <!-- brand mark placeholder -->
      <circle class="brand-dot" cx="466" cy="92" r="34" fill="var(--brand-green)"/>

      <!-- service band -->
      <rect class="band-services" x="0" y="170" width="560" height="226" fill="url(#bandGreen)"/>
      <!-- phone band -->
      <rect class="band-phone" x="0" y="396" width="540" height="72" fill="var(--band-yellow)"/>

      <!-- feature photo area -->
      <g role="img" aria-label="Photo of a flower bed with tulips and flowering shrubs">
        <circle cx="612" cy="285" r="200" fill="url(#photoTone)" stroke="var(--sign-white)" stroke-width="10"/>
      </g>

      <!-- bullets -->
      <g class="bullets" fill="var(--band-green-dark)">
        <circle cx="68" cy="218" r="9"/>
        <circle cx="226" cy="218" r="9"/>
        <circle cx="68" cy="282" r="9"/>
        <circle cx="68" cy="347" r="9"/>
      </g>

      <!-- phone icon -->
      <g class="phone-icon">
        <circle cx="80" cy="431" r="23" fill="var(--sign-white)" stroke="var(--band-green-dark)" stroke-width="4"/>
        <path d="M72 420 c-3 2 -4 6 -2 11 c2 6 6 11 11 13 c4 2 7 1 9 -2 l-4 -4 c-1 -1 -3 -1 -4 0 l-1 1 c-3 -1 -6 -4 -7 -7 l1 -1 c1 -1 1 -3 0 -4 z" fill="var(--band-green-dark)"/>
      </g>
    </svg>

    <div class="brand-name">Brightleaf<br>Outdoors</div>

    <ul class="services">
      <li class="service service--sod">SOD</li>
      <li class="service service--lawn">LAWN</li>
      <li class="service service--garden">GARDEN</li>
      <li class="service service--landscape">LANDSCAPE</li>
    </ul>

    <p class="phone">(555) 014-2377</p>
    <p class="tagline">Installation &amp; Delivery Available</p>
  </div>
</body>
</html>
```